Metal Fabrication Business Cards

We need a business card for our business of Metal Fabrication/Welding. Our company is called "Hadley's Metal Fabrication"

We are a metal fabrication business which takes on "high class" clients- dealing with some of the biggest builders in Australia. Our work is neat, and the type of work we do is 2nd to none for quality. We want to show that on our cards. However, we would love to show a side that is down to earth and a bit more modern and contemporary - we are all young in business so would love to show that side - rather than a boring "very straight looking" card. We always have a clean workshop and take pride in our presentation. We want to come across like we are very rich, but would love to go for a surf as well! A card that basically says we have high class and will charge you a high rate - but the quality will be outstanding.

Front of card: - Simply but sharp!
-Thinking maybe white card - with nice black writing.
-On the right hand side of card a person welding - or holding a welder.
- My business name - Hadley's Metal Fabrication
-Also maybe my name - which is 'Corey" (if it doesn't work, we can put this on the back of card.)
- if needed to look better - we can put keywords on front of card like "metal fabrication, sheet metal, welding etc" but I dont want it to be crowded.

Back of card: - Also make smart but sharp!
Put details such as:
04387 21 914
hadley.fabrication@tinmailbox.com.au
7/32 Keel Street
North Tarrin NSW 2471
www.korvinfabrication.com.au
ABN 72 615 803 914

thats just an idea - its now up to you. I don't mind what you come up with - as long as it stands out from the rest and looks sharp, professional but contemporary.

Business

Put details such as:
04387 21 914
7/32 Keel Street
North Tarrin NSW 2471
ABN 72 615 803 914

Hadley's Metal Fabrication

```html
<!DOCTYPE html>
<html lang="en">
<head>
<meta charset="utf-8">
<title>Hadley's Metal Fabrication – Business Cards</title>
<link href="https://fonts.googleapis.com/css2?family=Open+Sans:wght@400;700&display=swap" rel="stylesheet">
<style>
  :root {
    --backdrop: #141414;
    --card-light: #f3f3f3;
    --card-dark: #03050c;
    --brand-blue: #2a6fb8;
    --brand-red: #e8332a;
    --accent-red: #e5233d;
    --ink: #1d1d1d;
  }
  * { margin: 0; padding: 0; box-sizing: border-box; }
  html, body { width: 1200px; height: 900px; overflow: hidden; }
  body {
    background: var(--backdrop);
    font-family: "Open Sans", sans-serif;
    position: relative;
  }
  .card {
    position: absolute;
    top: 184px;
    height: 490px;
    border-radius: 14px;
    overflow: hidden;
  }
  .card--front { left: 299px; width: 301px; background: var(--card-light); }
  .card--back { left: 645px; width: 305px; background: var(--card-dark); }

  .brand {
    position: absolute;
    left: 0; right: 0;
    text-align: center;
  }
  .brand__mark {
    display: block;
    margin: 0 auto 12px;
  }
  .brand__name {
    font-weight: 700;
    color: var(--brand-blue);
    font-size: 26px;
    line-height: 1.12;
    letter-spacing: 0.5px;
    text-transform: uppercase;
  }
  .card--front .brand { top: 72px; }
  .card--back .brand { top: 42px; }
  .card--back .brand__mark { margin-bottom: 18px; }

  .contact {
    position: absolute;
    left: 0; right: 0;
    top: 254px;
    text-align: center;
    color: var(--ink);
    font-size: 13px;
    line-height: 17px;
  }
  .contact__name {
    color: var(--accent-red);
    font-weight: 700;
    font-size: 17px;
    line-height: 24px;
    letter-spacing: 0.5px;
    margin-bottom: 15px;
  }
  .contact__abn { margin-bottom: 9px; }
  .contact__label { color: var(--accent-red); }
  .contact__group { margin-bottom: 14px; }

  .work-photo {
    position: absolute;
    left: 0; right: 0; bottom: 0;
    height: 235px;
    background:
      radial-gradient(circle at 72% 75%, rgba(220,230,255,0.95) 0, rgba(140,160,230,0.55) 12%, rgba(60,70,140,0.25) 32%, transparent 55%),
      radial-gradient(circle at 38% 30%, rgba(120,130,160,0.5) 0, transparent 40%),
      linear-gradient(to bottom, var(--card-dark) 0%, #141a2e 45%, #232c4a 100%);
  }
</style>
</head>
<body>

  <section class="card card--front">
    <div class="brand">
      <svg class="brand__mark" width="60" height="60" viewBox="0 0 60 60" aria-hidden="true">
        <circle cx="30" cy="30" r="26" fill="none" stroke="var(--brand-red)" stroke-width="4"/>
      </svg>
      <p class="brand__name">Hadley's<br>Metal Fabrication</p>
    </div>
    <div class="contact">
      <p class="contact__name">COREY</p>
      <p class="contact__abn"><span class="contact__label">ABN:</span> 72 615 803 914</p>
      <p class="contact__group">7/32 Keel Street<br>North Tarrin NSW 2471</p>
      <p>04387 21 914<br>hadley.fabrication@tinmailbox.com.au<br>www.korvinfabrication.com.au</p>
    </div>
  </section>

  <section class="card card--back">
    <div class="brand">
      <svg class="brand__mark" width="70" height="70" viewBox="0 0 70 70" aria-hidden="true">
        <circle cx="35" cy="35" r="31" fill="none" stroke="var(--brand-red)" stroke-width="4"/>
      </svg>
      <p class="brand__name">Hadley's<br>Metal Fabrication</p>
    </div>
    <div class="work-photo" role="img" aria-label="Photo of a welder in a helmet welding metal, with bright sparks flying"></div>
  </section>

</body>
</html>
```